Design the Mobile Version of Existing Web Based Health Platform

Loomcrest is a social business enterprise that focus on public health by applying innovative healthcare services and consumer internet technology. Loomcrest offers a personalized platform of health promotion and disease prevention that puts the individual back in control of his life.

Loomcrest is looking for a Mobile Web UX/Visual Design professional to create a mobile version of Loomcrest website platform for iPhone, Tablet/tablet and Android.

Contestants must to check www.loomcrest-demo.com.br to have a better understanding of Loomcrest Platform by creating an account (it's in portuguese, but anyone can get the general idea).

The mobile version of Loomcrest should have very similar functionality and user flows. This job is not to reengineer or re-imagine Loomcrest. It is just to reformat the existing functionality so it works well on mobile devices.

This description below is to help you to understand the core features of the platform (check the attachments to see the new web design of each one):

- Personally Controlled Health Record - PCHR enables an individual to own and manage a complete, secure, digital copy of her health and wellness information.
- Health Risk Assessments - is a process to estimate the nature and probability of adverse health effects, based on personal and family historical data, behavior and environment.
- Simulation of future health - "what if analysis" that emphasizes health education and behavior change.
- Step Quests - a program that gives you the opportunity to the participant to advance his personal well-being by doing simple Step Quests
- Health Alerts and Recommendations and Missing Data - Recommendations based on Wellbeing Bureau Guidelines and Federal Wellness Review Panel (FWRP), plus notifications to update outdated information.

The deliverable for this project is a psd file with a designed mobile version of Loomcrest.

A new design of the web platform is under construction. You can also check it looking at the files attached.

Target Market(s)

people 25-40 years old, 60% female, socially engaged

Industry/Entity Type

Healthcare

Requirements
Must have
• iPhone, Tablet and Android version

Design must cover all current functionalities available on the web version (please, ensure you understand all features by creating an account at www.loomcrest-demo.com.br)

- Login/Sign up
- Welcome (first assessment)
- Add to Personal Controlled Health Record (PCHR)
- Update/Remove PCHR
- List PCHR
- Riskgrid (risk assessmen results)
- Simulation
- Alerts
- Missing data
- Recommendations
- StepQuest
- Badges
- Configurations

It's important to check the attachments to see how the web platform design is evolving.

```html
<!DOCTYPE html>
<html lang="en">
<head>
<meta charset="utf-8">
<title>Loomcrest – Health Map (tablet)</title>
<link rel="stylesheet" href="https://fonts.googleapis.com/css2?family=Arimo:wght@400;700&display=swap">
<style>
  :root {
    --stage: #e9e6e2;
    --status: #111214;
    --sidebar: #2a2c30;
    --sidebar-line: #35383d;
    --sidebar-active: #34373c;
    --panel-dark: #2f3135;
    --card: #26282b;
    --green: #8cc63f;
    --green-dark: #6fa82a;
    --orange: #f47b20;
    --orange-soft: #f9a55c;
    --red: #d7263d;
    --yellow: #f5d327;
    --lime: #a6d34a;
    --moss: #5c8f2a;
    --text-light: #e8e8e8;
    --text-muted: #9a9ca0;
    --table-bg: #e9ebee;
    --row-bg: #ffffff;
    --row-line: #cfd2d6;
    --text-dark: #3b3d41;
  }
  * { box-sizing: border-box; margin: 0; padding: 0; }
  html, body { width: 1200px; height: 765px; overflow: hidden; }
  body { background: var(--stage); font-family: "Arimo", Helvetica, Arial, sans-serif; position: relative; }

  .app { position: absolute; left: 100px; top: 7px; width: 1000px; height: 750px; background: var(--panel-dark); overflow: hidden; }

  .status-bar { position: absolute; inset: 0 0 auto 0; height: 20px; background: var(--status); color: #fff; font-size: 11px; display: flex; align-items: center; justify-content: space-between; padding: 0 8px; }
  .status-bar .time { font-weight: 700; }

  /* Sidebar */
  .sidebar { position: absolute; left: 0; top: 20px; bottom: 0; width: 250px; background: var(--sidebar); color: var(--text-light); }
  .profile { display: flex; align-items: center; gap: 10px; height: 44px; padding: 0 10px; border-bottom: 1px solid var(--sidebar-line); }
  .avatar { width: 30px; height: 30px; border-radius: 3px; background: linear-gradient(135deg, #d9896a, #a9553c); }
  .profile-name { font-weight: 700; font-size: 14px; }
  .nav { list-style: none; }
  .nav-item { position: relative; display: flex; align-items: center; gap: 12px; height: 44px; padding: 0 14px; font-size: 13px; font-weight: 700; border-bottom: 1px solid var(--sidebar-line); }
  .nav-item svg { width: 20px; height: 20px; flex: none; }
  .nav-item.is-active { background: var(--sidebar-active); color: var(--orange); }
  .nav-badge { position: absolute; right: 14px; width: 22px; height: 22px; border-radius: 50%; background: var(--red); color: #fff; font-size: 12px; display: flex; align-items: center; justify-content: center; border: 2px solid #fff; }
  .nav-arrow { position: absolute; right: 14px; color: var(--orange); }
  .copyright { padding: 14px; font-size: 9px; color: #6c6f74; line-height: 1.4; }
  .sidebar-decor { position: absolute; left: 0; right: 0; bottom: 0; height: 190px; background: linear-gradient(180deg, rgba(42,44,48,0) 0%, #25272a 100%); }

  /* Main */
  .main { position: absolute; left: 250px; right: 0; top: 20px; bottom: 0; }
  .topbar { height: 44px; background: linear-gradient(180deg, #9ad44a, var(--green-dark)); display: flex; align-items: center; position: relative; }
  .menu-btn { display: flex; align-items: center; gap: 6px; padding-left: 12px; }
  .menu-badge { width: 20px; height: 20px; border-radius: 50%; background: var(--red); color: #fff; font-size: 11px; display: flex; align-items: center; justify-content: center; border: 2px solid #fff; }
  .topbar-title { position: absolute; left: 0; right: 0; text-align: center; color: #fff; font-size: 17px; font-weight: 700; text-shadow: 0 -1px 0 rgba(0,0,0,.2); }
  .add-btn { position: absolute; right: 0; top: 0; width: 44px; height: 44px; background: var(--green-dark); border-left: 1px solid rgba(255,255,255,.25); color: #fff; font-size: 26px; display: flex; align-items: center; justify-content: center; }

  .overview { position: relative; height: 286px; }
  .body-map { position: absolute; left: 50px; top: 20px; width: 150px; height: 250px; }
  .body-figure { position: absolute; left: 20px; top: 50px; width: 110px; height: 200px; border-radius: 50px 50px 10px 10px; background: linear-gradient(180deg, #3a3d42, #33363a); }
  .risk-donut { position: absolute; left: 38px; top: 0; }

  .risk-card { position: absolute; left: 250px; top: 18px; width: 470px; background: var(--card); border-radius: 4px; padding: 14px 16px; color: var(--text-light); }
  .risk-level { color: var(--orange); font-size: 15px; font-weight: 700; }
  .risk-compare { font-size: 13px; margin-top: 4px; }
  .risk-note { font-size: 10px; color: var(--text-muted); line-height: 1.35; margin-top: 6px; }
  .reduce { margin-top: 12px; font-size: 10px; color: var(--text-muted); }
  .reduce strong { color: var(--text-light); }
  .actions { display: flex; gap: 18px; margin-top: 8px; }
  .action { display: flex; align-items: center; gap: 6px; color: var(--green); font-weight: 700; font-size: 12px; line-height: 1.15; }
  .tick { width: 22px; height: 22px; background: var(--green); border-radius: 2px; display: flex; align-items: center; justify-content: center; flex: none; }

  .legend { position: absolute; left: 250px; top: 196px; display: grid; grid-template-columns: 180px 180px; row-gap: 6px; font-size: 11px; color: var(--text-muted); }
  .legend-item { display: flex; align-items: center; gap: 8px; }
  .dot { width: 10px; height: 10px; border-radius: 50%; }

  .risks { position: absolute; left: 0; right: 0; top: 330px; bottom: 0; background: var(--table-bg); padding: 20px 50px 0 40px; }
  .risks-title { text-align: center; font-size: 14px; font-weight: 700; color: var(--text-dark); margin-bottom: 12px; }
  .risk-row { display: flex; align-items: center; justify-content: space-between; height: 34px; margin-bottom: 8px; background: var(--row-bg); border: 1px solid var(--row-line); padding: 0 12px; font-size: 13px; color: var(--text-dark); }
  .risk-row.is-top { background: var(--orange); border-color: var(--orange); color: #fff; font-weight: 700; }
  .risk-value { border-left: 1px solid var(--row-line); padding-left: 12px; min-width: 56px; text-align: right; }
  .risk-row.is-top .risk-value { border-left-color: rgba(255,255,255,.4); }
  .help { display: inline-flex; width: 18px; height: 18px; border-radius: 50%; background: var(--orange-soft); color: #fff; font-size: 11px; align-items: center; justify-content: center; margin-left: 8px; border: 1px solid #fff; }
  .scrollbar { position: absolute; right: 20px; top: 60px; width: 5px; height: 220px; border-radius: 3px; background: #b8bcc2; }
</style>
</head>
<body>
<div class="app">
  <div class="status-bar"><span>Tablet</span><span class="time">4:20 PM</span><span>▮▮▮</span></div>

  <aside class="sidebar">
    <div class="profile">
      <div class="avatar" role="img" aria-label="User profile photo"></div>
      <span class="profile-name">Jonathan</span>
    </div>
    <ul class="nav">
      <li class="nav-item is-active">
        <svg viewBox="0 0 20 20"><circle cx="10" cy="5" r="3" fill="currentColor"/><path d="M5 18v-6a5 5 0 0 1 10 0v6z" fill="currentColor"/></svg>
        Health Map <span class="nav-badge">5</span>
      </li>
      <li class="nav-item">
        <svg viewBox="0 0 20 20" fill="none" stroke="#c8c9cc" stroke-width="1.6"><circle cx="10" cy="5" r="3"/><path d="M5 18v-6a5 5 0 0 1 10 0v6"/></svg>
        Simulation <span class="nav-arrow">›</span>
      </li>
      <li class="nav-item">
        <svg viewBox="0 0 20 20" fill="none" stroke="#c8c9cc" stroke-width="1.6"><circle cx="10" cy="10" r="7"/><path d="M7 10l2 2 4-4"/></svg>
        Challenges
      </li>
      <li class="nav-item">
        <svg viewBox="0 0 20 20" fill="none" stroke="#c8c9cc" stroke-width="1.6"><rect x="4" y="3" width="12" height="14" rx="1"/><path d="M7 7h6M7 10h6M7 13h4"/></svg>
        Records
      </li>
      <li class="nav-item">
        <svg viewBox="0 0 20 20" fill="none" stroke="#c8c9cc" stroke-width="1.6"><path d="M6 3h8v5a4 4 0 0 1-8 0zM10 12v3M7 17h6"/></svg>
        Trophies
      </li>
      <li class="nav-item">
        <svg viewBox="0 0 20 20" fill="#c8c9cc"><rect x="3" y="3" width="4" height="4"/><rect x="8" y="3" width="4" height="4"/><rect x="13" y="3" width="4" height="4"/><rect x="3" y="8" width="4" height="4"/><rect x="8" y="8" width="4" height="4"/><rect x="13" y="8" width="4" height="4"/><rect x="3" y="13" width="4" height="4"/><rect x="8" y="13" width="4" height="4"/><rect x="13" y="13" width="4" height="4"/></svg>
        More
      </li>
    </ul>
    <p class="copyright">© Copyright 2013 – Loomcrest<br>All rights reserved.</p>
    <div class="sidebar-decor" role="img" aria-label="Faint background pattern of sport and health icons"></div>
  </aside>

  <main class="main">
    <header class="topbar">
      <div class="menu-btn">
        <svg width="18" height="14" viewBox="0 0 18 14" fill="#fff"><rect width="18" height="2.5"/><rect y="5.5" width="18" height="2.5"/><rect y="11" width="18" height="2.5"/></svg>
        <span class="menu-badge">5</span>
      </div>
      <h1 class="topbar-title">Health Map</h1>
      <div class="add-btn">+</div>
    </header>

    <section class="overview">
      <div class="body-map">
        <div class="body-figure" role="img" aria-label="Outline of a human body with risk markers on the head, chest and abdomen"></div>
        <svg class="risk-donut" width="74" height="74" viewBox="0 0 74 74">
          <circle cx="37" cy="37" r="30" fill="none" stroke="#ffffff" stroke-width="6"/>
          <circle cx="37" cy="37" r="30" fill="none" stroke="#f47b20" stroke-width="6" stroke-dasharray="113.1 188.5" transform="rotate(-90 37 37)"/>
          <text x="37" y="43" text-anchor="middle" font-family="Arimo, sans-serif" font-size="18" font-weight="700" fill="#f47b20">60%</text>
        </svg>
      </div>

      <div class="risk-card">
        <p class="risk-level">Above average</p>
        <p class="risk-compare">60% of men this age have a lower risk.</p>
        <p class="risk-note">It is important to know, more accurately, the risk of you being diagnosed with stroke in the next 5 years. To do this, delete the data pending the notebook.</p>
        <p class="reduce">Reduce your risk by <strong>30%</strong></p>
        <div class="actions">
          <span class="action"><span class="tick"><svg width="14" height="12" viewBox="0 0 14 12"><path d="M1 6l4 4 8-9" fill="none" stroke="#fff" stroke-width="2.5"/></svg></span>Practice<br>Physical Activity</span>
          <span class="action"><span class="tick"><svg width="14" height="12" viewBox="0 0 14 12"><path d="M1 6l4 4 8-9" fill="none" stroke="#fff" stroke-width="2.5"/></svg></span>Stop Smoking</span>
          <span class="action"><span class="tick"><svg width="14" height="12" viewBox="0 0 14 12"><path d="M1 6l4 4 8-9" fill="none" stroke="#fff" stroke-width="2.5"/></svg></span>Stop Smoking</span>
        </div>
      </div>

      <div class="legend">
        <span class="legend-item"><span class="dot" style="background:var(--orange)"></span>Pre-existing condition</span>
        <span class="legend-item"><span class="dot" style="background:var(--yellow)"></span>On Average</span>
        <span class="legend-item"><span class="dot" style="background:var(--red)"></span>High risk</span>
        <span class="legend-item"><span class="dot" style="background:var(--lime)"></span>Below Average</span>
        <span class="legend-item"><span class="dot" style="background:var(--orange-soft)"></span>Above Average</span>
        <span class="legend-item"><span class="dot" style="background:var(--moss)"></span>Low</span>
      </div>
    </section>

    <section class="risks">
      <h2 class="risks-title">Your Risks</h2>
      <div class="risk-row is-top"><span>Risk of Coronary Disease<span class="help">?</span></span><span class="risk-value">60%</span></div>
      <div class="risk-row"><span>Risk of Diabetes</span><span class="risk-value">0.6%</span></div>
      <div class="risk-row"><span>Risk of Stroke</span><span class="risk-value">0.6%</span></div>
      <div class="risk-row"><span>Risk of Lung Cancer</span><span class="risk-value">0.6%</span></div>
      <div class="risk-row"><span>Risk of Lung Disease</span><span class="risk-value">0.6%</span></div>
      <div class="scrollbar"></div>
    </section>
  </main>
</div>
</body>
</html>
```